Vorlan cards

I am in the auto motive, transportation business I would like a business card that is Something cool, modern edgy, having to do with car culture. I offer towing service for high and exotic cars. I also provide towing for collisions and car accidents. I offer open and enclosed transport nationwide.

Target Market(s)

Car culture people high end auto collectors

Industry/Entity Type

Towing car carrier

Contact Information for Business Card

My company colors black yellow and silver

Font styles to use
Serif

```html
<!DOCTYPE html>
<html lang="en">
<head>
<meta charset="utf-8">
<title>Vorlan Cards</title>
<link href="https://fonts.googleapis.com/css2?family=Arimo:wght@400;700&display=swap" rel="stylesheet">
<style>
  :root {
    --bg: #e9e9e9;
    --paper: #ffffff;
    --ink: #111111;
    --muted: #8a8a8a;
    --rule: #555555;
    --yellow: #f2cf2e;
    --charcoal: #323232;
    --charcoal-deep: #1a1a1a;
    --silver: #6b6b6b;
  }
  * { box-sizing: border-box; margin: 0; padding: 0; }
  html, body { width: 1200px; height: 802px; overflow: hidden; }
  body {
    background: var(--bg);
    font-family: "Arimo", Arial, sans-serif;
    position: relative;
  }
  .card {
    position: absolute;
    width: 525px;
    height: 300px;
    border-bottom: 4px solid var(--yellow);
    border-right: 3px solid var(--yellow);
    box-shadow: 0 14px 30px rgba(0,0,0,.18);
    overflow: hidden;
  }
  .card-front { left: 55px; top: 110px; background: var(--paper); }
  .card-back { left: 620px; top: 392px; background: var(--charcoal); }

  .brand {
    position: absolute;
    display: flex;
    align-items: center;
    gap: 10px;
    font-weight: 700;
    letter-spacing: 3px;
    white-space: nowrap;
  }
  .brand-mark { width: 22px; height: 22px; background: var(--yellow); flex: none; }
  .card-front .brand { right: 46px; top: 48px; font-size: 38px; color: var(--ink); }

  .rule {
    position: absolute;
    left: 40px; right: 40px; top: 182px;
    height: 1px; background: var(--rule);
  }
  .holder { position: absolute; left: 40px; top: 136px; }
  .holder-name { font-size: 21px; font-weight: 700; color: var(--ink); letter-spacing: .5px; }
  .holder-role { font-size: 14px; color: var(--muted); margin-top: 2px; }

  .address {
    position: absolute; right: 46px; top: 138px;
    text-align: right; font-size: 14px; line-height: 1.3; color: var(--muted);
  }
  .contacts { position: absolute; left: 40px; top: 198px; list-style: none; }
  .contacts li {
    display: flex; align-items: center; gap: 10px;
    font-size: 15px; color: var(--muted); line-height: 25px;
  }
  .contacts svg { width: 13px; height: 13px; fill: var(--ink); }

  .card-back .brand { left: 28px; top: 124px; font-size: 28px; letter-spacing: 2px; color: var(--yellow); }
  .truck-art {
    position: absolute; right: 0; bottom: 0;
    width: 250px; height: 230px;
    background: linear-gradient(135deg, var(--silver) 0%, var(--charcoal-deep) 70%);
    opacity: .85;
    border-top-left-radius: 40px;
  }
</style>
</head>
<body>
  <section class="card card-front">
    <div class="brand"><span class="brand-mark"></span>VORLAN</div>
    <div class="holder">
      <p class="holder-name">MARCUS HALE</p>
      <p class="holder-role">Manager</p>
    </div>
    <p class="address">Your Address, City<br>State, Zip 0000</p>
    <div class="rule"></div>
    <ul class="contacts">
      <li><svg viewBox="0 0 16 16"><path d="M3 1l3 3-2 2c1 2 3 4 5 5l2-2 3 3-2 2C7 14 2 9 1 3z"/></svg>555-214-7300</li>
      <li><svg viewBox="0 0 16 16"><path d="M1 3h14v10H1z M1 3l7 6 7-6" fill="none" stroke="#111" stroke-width="2"/></svg>dispatch@vorlanmail.com</li>
      <li><svg viewBox="0 0 16 16"><circle cx="8" cy="8" r="7"/></svg>www.vorlantow.com</li>
    </ul>
  </section>

  <section class="card card-back">
    <div class="brand"><span class="brand-mark"></span>VORLAN</div>
    <div class="truck-art" role="img" aria-label="Embossed silhouette of a flatbed tow truck in glossy black"></div>
  </section>
</body>
</html>
```